Electrical needs letterhead design

Need a letterhead design for an electrical company. Using the same colours as to what are used in the logo.
After a modern design.

Want the logo in top right or top left.

Must include...

ABN 71 804 239 356
PHONE 0458203917
www.kelmaroo.com.au
jed@kelmaroo.com.au

'ABN' and 'PHONE' in bold.

Keep it basic. Logo top left, details either next to it or far right corner. Dont want any other objects included.

Electrical

```html
<!DOCTYPE html>
<html lang="en">
<head>
<meta charset="utf-8">
<title>Kelmaroo Letterhead</title>
<link href="https://fonts.googleapis.com/css2?family=Open+Sans:wght@400;600;700&display=swap" rel="stylesheet">
<style>
  :root {
    --backdrop: #dcdcdc;
    --paper: #f7f7f7;
    --brand-red: #a3272a;
    --brand-red-light: #d84a35;
    --text: #555555;
    --icon: #c0392b;
  }
  * { box-sizing: border-box; margin: 0; padding: 0; }
  html, body {
    width: 1200px;
    height: 968px;
    overflow: hidden;
    background: var(--backdrop);
    font-family: "Open Sans", Arial, sans-serif;
  }
  .canvas {
    width: 1200px;
    height: 968px;
    display: flex;
    align-items: center;
    justify-content: center;
  }
  .letterhead {
    position: relative;
    width: 640px;
    height: 905px;
    background: var(--paper);
    box-shadow: 0 6px 24px rgba(0,0,0,0.12);
  }
  .top-band {
    height: 10px;
    background: linear-gradient(90deg, var(--brand-red), var(--brand-red-light));
  }
  .contact-list {
    position: absolute;
    top: 36px;
    left: 36px;
    list-style: none;
    font-size: 9.5px;
    line-height: 15px;
    color: var(--text);
  }
  .contact-list li {
    display: flex;
    align-items: center;
    gap: 6px;
  }
  .contact-list svg { width: 9px; height: 9px; flex: none; }
  .contact-list .label { font-weight: 700; }
  .contact-list .no-icon { padding-left: 15px; }
  .brand {
    position: absolute;
    top: 78px;
    right: 40px;
    display: flex;
    align-items: center;
    gap: 8px;
  }
  .brand-dot {
    width: 12px;
    height: 12px;
    border-radius: 50%;
    background: var(--brand-red);
  }
  .brand-name {
    font-size: 32px;
    font-weight: 600;
    color: var(--brand-red);
    letter-spacing: -0.5px;
  }
</style>
</head>
<body>
  <main class="canvas">
    <article class="letterhead">
      <div class="top-band"></div>

      <ul class="contact-list">
        <li>
          <svg viewBox="0 0 10 10" aria-hidden="true"><circle cx="5" cy="5" r="4.5" fill="none" stroke="var(--icon)"/><path d="M3.3 2.8 L4.2 2.6 L4.6 3.9 L4 4.3 Q4.6 5.6 5.8 6.1 L6.2 5.5 L7.4 5.9 L7.2 6.8 Q4 7.3 3.3 2.8Z" fill="var(--icon)"/></svg>
          <span>0458203917</span>
        </li>
        <li>
          <svg viewBox="0 0 10 10" aria-hidden="true"><circle cx="5" cy="5" r="4.5" fill="var(--icon)"/><rect x="3" y="3" width="4" height="4" fill="#fff"/></svg>
          <span><span class="label">ABN</span> 71 804 239 356</span>
        </li>
        <li>
          <svg viewBox="0 0 10 10" aria-hidden="true"><circle cx="5" cy="5" r="4.5" fill="var(--icon)"/><rect x="2.6" y="3.3" width="4.8" height="3.4" fill="#fff"/><path d="M2.6 3.3 L5 5.2 L7.4 3.3" fill="none" stroke="var(--icon)" stroke-width="0.6"/></svg>
          <span>jed@kelmaroo.com.au</span>
        </li>
        <li class="no-icon"><span>www.kelmaroo.com.au</span></li>
      </ul>

      <div class="brand">
        <span class="brand-dot"></span>
        <span class="brand-name">Kelmaroo</span>
      </div>
    </article>
  </main>
</body>
</html>
```